Website for a financial survey consultancy

WHO WE ARE
We're a niche HR consultancy specialising in salary comparison surveys for the financial asset management industry. We position ourselves as a small, highly responsive organisation with a strong personal relationship with each of our 50+ blue-chip clients.

WHAT WE DO
Our business is 80% surveys (= products), 20% consultancy (= services). The surveys are a set of online products which clients interact with to find the information they are interested in.

WHAT WE WANT
We are completely revising our existing marketing website and need a new up-to-date look and feel for the site. We want you to design 2 web pages
- Home page
- Internal content page

More details below in Must Have Priorities.

REFERENCE SITES
- www.tallowmere.com - nice background image
- www.quimbelt.com - ignoring the animations
- www.palvastro.com
- www.dulmiko.com - clean, fresh, styly but prob not corporate enough
- www.orvettagrove.com - spacious, beautiful, slightly dated tho
- www.plinzer.co.uk - ignore the colours. Like the simplicity, larger font size (although want to stick with sans-serif fonts for main content)

DELIVERABLES
The final designs should be delivered as one or more PSD files with clearly named layers. All design elements and treatments should be separated out, for example use adjustment layers rather than applied (and subsequently irreversible) adjustments, strokes, shading, etc.

WHAT NEXT
I'll be monitoring the contest every day and can respond to questions fast. You can IM me on Skype or MSN.

Reason: Hi folks,

I am extending the deadline to this project as I am travelling this week and therefore will not be able to make a final decision until next Monday. I will try and provide further feedback over the course of this week but I am only going to be online occasionally so be prepared to wait a few days for a reply from me.

Thanks for all the designs so far.

Owen

Target Market(s)

In order of importance, most important first

1. Potential customers - UK & US financial industry HR professionals, short on time. Heard about us already, want to find out more about what we do, confirm relevance for their needs. Core goal - establish credibility: are we properly resourced, will we be around for years to come, are we *real*.

2. Existing customers - UK & US financial industry professionals, short on time, under pressure, want results quickly, minimum faff, expect high quality, slickly presented information. Primary action: login and use surveys.

3. Industry professionals/researchers - probably arriving through blog content, looking to browse and hoover information. Valuable for their ability to spread awareness of who we are amongst their peers.

Industry/Entity Type

Financial

Requirements
Must have
• GENERAL
Style cues - Corporate, professional, financial, stylish, slick, clean, spacious, light
Size - standard 960px grid

NAVIGATION
- [ Home | About us | Surveys | Consulting | Blog ]
- Sub-nav (roll-over dropdown) on About Us, Surveys & Consulting

ALL PAGES
- Site navigation
- Client login (on screen permanently or link to ajaxy in-page pop-up)
- Footer section
- Existing logo (attached)* - this is obviously an important reference point in the design, esp colour

HOME PAGE
- Communicate (link thru to?) survey/consulting split
- Large photo(s)/backdrop (2-3 interchangeable options ideally). Please consider what rights agreement will be necessary for any photos you include in your design.
- Possibly bigger more prominent version of logo
- Strap line/sentence - "Focussed data is the key to success"
- 3 recent blog posts (should look good with and without blog post images)
- Free downloadable PDF research report + supporting blurb

INTERNAL PAGE
- Page title
- Content - typical page will be less than one screenfull
- Level 1 sub-heading
- Level 2 sub-heading
- Bulleted list
- Content supporting image (any image will do - interested in placement, borders (if any), spacing, caption, etc)
- 'Do something' button

* Note: there is some internal debate about this logo at the moment. Some (me) are keen for it to change, some (not me!) are not. If you have an web page design idea/concept that requires an evolution of the logo, go ahead and evolve it. We can explore this further in the design process as necessary, but don't sweat it.
Nice to have
• Values to communicate
- Knowledgeable
- Professional
- Secure
- Personal
- Experienced
- Financial industry specific
- Accurate
- Reliable
Should not have
• - Search box
- Social media links, other than RSS feed button (discrete)

```html
<!DOCTYPE html>
<html lang="en">
<head>
<meta charset="utf-8">
<title>Korvane Consulting</title>
<link rel="stylesheet" href="https://fonts.googleapis.com/css2?family=Arimo:wght@400;700&family=Open+Sans:wght@400&display=swap">
<style>
:root{
  --canvas:#464646;
  --page:#ffffff;
  --brand:#6e0b0b;
  --brand-deep:#5a0707;
  --text:#3a3a3a;
  --nav-top:#3a3a3a;
  --nav-bottom:#141414;
  --nav-divider:#555;
  --rule:#9a9a9a;
  --field-border:#c9c9c9;
}
*{margin:0;padding:0;box-sizing:border-box}
html,body{width:1200px;height:594px;overflow:hidden}
body{background:var(--canvas);font-family:"Arimo",Arial,sans-serif;color:var(--text);position:relative}
.page{position:absolute;left:115px;top:0;width:970px;height:560px;background:var(--page)}
.brand{position:absolute;left:5px;top:0;width:108px;height:235px;background:#fff}
.brand-square{width:108px;height:105px;background:var(--brand)}
.brand-name{display:block;margin-top:26px;text-align:center;font-size:25px;color:var(--brand);font-weight:400}
.brand-base{position:absolute;left:0;bottom:0;width:108px;height:8px;background:linear-gradient(#d8d8d8,#a8a8a8)}
.hero{position:absolute;left:123px;top:0;width:842px;height:216px;
  background:linear-gradient(90deg,#ecebe8 0%,#f4f5f6 30%,#dfe6ee 55%,#c9d2dc 75%,#2f3440 100%)}
.hero-line{position:absolute;left:123px;top:216px;width:842px;height:2px;background:var(--brand)}
.hero-base{position:absolute;left:123px;top:218px;width:842px;height:17px;background:linear-gradient(#f2f2f2,#b9b9b9)}
.strapline{position:absolute;left:278px;top:172px;font-family:"Open Sans",Arial,sans-serif;font-size:23px;color:#1e1e28;letter-spacing:-.2px}
.nav{position:absolute;left:5px;top:237px;width:960px;height:38px;background:linear-gradient(var(--nav-top),var(--nav-bottom));display:flex}
.nav a{display:block;height:38px;line-height:38px;text-align:center;color:#fff;text-decoration:none;font-size:14px;border-right:1px solid var(--nav-divider)}
.nav a.active{background:linear-gradient(#8a0f0f,#5c0505)}
.nav .report{position:absolute;right:10px;top:0;line-height:38px;color:#fff;font-size:13px}
.nav .report b{font-weight:700}
.content-fade{position:absolute;left:5px;top:275px;width:960px;height:30px;background:linear-gradient(#e2e2e2,#fff)}
.intro{position:absolute;left:27px;top:296px;width:700px}
.intro h1{font-size:26px;font-weight:400;color:var(--brand);letter-spacing:-.3px;margin-bottom:9px}
.intro p{font-size:12px;line-height:15px;margin-left:2px;margin-bottom:15px}
.questions{list-style:none;margin:22px 0 0 23px}
.questions li{font-size:12px;line-height:21px;color:var(--brand);display:flex;align-items:center}
.questions svg{margin-right:9px}
.login{position:absolute;left:745px;top:290px;width:207px;height:183px;background:linear-gradient(#fff 60%,#eef2f4);border-radius:5px;box-shadow:0 0 4px rgba(0,0,0,.35);padding:9px 15px 0 14px}
.login h2{font-size:20px;font-weight:400;color:var(--brand-deep);padding-bottom:2px;border-bottom:2px solid transparent;
  border-image:linear-gradient(90deg,#555,#ccc 80%,transparent) 1}
.login label{display:block;font-size:14px;color:#222;margin-top:11px}
.login label:first-of-type{margin-top:10px}
.login .field{display:block;width:170px;height:19px;border:1px solid var(--field-border);background:#fff;margin-top:2px}
.login button{margin-top:12px;width:76px;height:23px;border:0;background:linear-gradient(#8a0c0c,#5e0404);color:#fff;font-family:inherit;font-size:14px;text-align:left;padding-left:6px}
.footer{position:absolute;left:117px;top:567px;width:969px;display:flex;justify-content:space-between;font-size:12px;color:#fff}
.footer nav a{color:#fff;text-decoration:none}
.footer nav span{margin:0 5px}
</style>
</head>
<body>
<div class="page">
  <div class="brand">
    <div class="brand-square"></div>
    <span class="brand-name">Korvane</span>
    <div class="brand-base"></div>
  </div>
  <div class="hero" role="img" aria-label="Photo of a hand working figures with a pen and calculator beside a team of business people in a meeting"></div>
  <div class="strapline">Focussed data is the key to success</div>
  <div class="hero-line"></div>
  <div class="hero-base"></div>

  <nav class="nav">
    <a href="#" style="width:86px">HOME</a>
    <a href="#" style="width:117px">ABOUT US</a>
    <a href="#" class="active" style="width:101px">SURVEYS</a>
    <a href="#" style="width:141px">CONSULTING</a>
    <a href="#" style="width:81px">BLOG</a>
    <span class="report">Free downloadable <b>Research Report</b></span>
  </nav>
  <div class="content-fade"></div>

  <section class="intro">
    <h1>Welcome to Our Website</h1>
    <p>Korvane Consulting is at the forefront in developing and implementing innovative approaches to the remuneration issues facing senior management in financial services.</p>
    <p>We conduct both regular and ad hoc research into remuneration and reward issues. The surveys have been designed, in close consultation with leading firms, to provide you with vital sector-specific information and data to help your firm answer these key questions:</p>
    <ul class="questions">
      <li><svg width="5" height="7" viewBox="0 0 5 7"><path d="M0 0L5 3.5L0 7z" fill="#6e0b0b"/></svg>Are we really performance driven?</li>
      <li><svg width="5" height="7" viewBox="0 0 5 7"><path d="M0 0L5 3.5L0 7z" fill="#6e0b0b"/></svg>Are we getting value for money from our remuneration spend?</li>
      <li><svg width="5" height="7" viewBox="0 0 5 7"><path d="M0 0L5 3.5L0 7z" fill="#6e0b0b"/></svg>Should we pay commissions to sales people?</li>
      <li><svg width="5" height="7" viewBox="0 0 5 7"><path d="M0 0L5 3.5L0 7z" fill="#6e0b0b"/></svg>What is the most effective balance between short and long term remuneration?</li>
      <li><svg width="5" height="7" viewBox="0 0 5 7"><path d="M0 0L5 3.5L0 7z" fill="#6e0b0b"/></svg>What are other firms doing on remuneration to get a competitive edge?</li>
    </ul>
  </section>

  <aside class="login">
    <h2>Login</h2>
    <label>Name</label>
    <span class="field"></span>
    <label>Email Id</label>
    <span class="field"></span>
    <button type="button">Submit</button>
  </aside>
</div>

<footer class="footer">
  <nav><a href="#">Home</a><span>I</span><a href="#">About us</a><span>I</span><a href="#">Surveys</a><span>I</span><a href="#">Consulting</a><span>I</span><a href="#">Blog</a></nav>
  <div>Copyright @ 2011 Korvane</div>
</footer>
</body>
</html>
```